Maple Dental Centre Kelvona business cards and presentation folder

dental practice needing innovative black business cards for 2 different dentists witrh appointment details written at the back of the card for the patient.
name of dentists: Dr Priyanka R Valtenhoff B.D.Sc., M.Sc (Kelv)
Dr. Tom Garvel B.D.S.

Target Market(s)

professioinal, working class

Industry/Entity Type

Dental Clinic

Contact Information for Business Card

Dr. Tom Garvel B.D.S.

Font styles to use
Sans Serif

Requirements
Must have
• Front side: logo
• dentist name
• phone number: 07- 5581 2943
• back side: appointment details: date, time,
• Address: 117C, 48 Harlow Street, Kelvona - 4821, Queensland
• Email: admin@mapledentalcentrekelvona.example.au
• Website: www.mapledentalcentre.example.au
• preferable logo colors
Nice to have
• classy look more pleasing

```html
<!DOCTYPE html>
<html lang="en">
<head>
<meta charset="utf-8">
<title>Maple Dental Centre Kelvona – Business Card</title>
<link rel="stylesheet" href="https://fonts.googleapis.com/css2?family=Open+Sans:wght@400;600;700&display=swap">
<style>
  :root {
    --bg: #d9d6d2;
    --card-dark: #232122;
    --card-light: #ececec;
    --green: #72a84a;
    --grey: #8f979b;
    --text-light: #c9cbcc;
    --text-dark: #3a3a3a;
  }
  * { margin: 0; padding: 0; box-sizing: border-box; }
  html, body {
    width: 1200px; height: 900px; overflow: hidden;
    background: var(--bg);
    font-family: "Open Sans", Arial, sans-serif;
  }
  .stage {
    width: 1200px; height: 900px;
    display: flex; flex-direction: column; align-items: center; justify-content: center;
    gap: 44px;
  }
  .card {
    position: relative; width: 640px; height: 391px; overflow: hidden;
    box-shadow: 0 6px 18px rgba(0,0,0,.18);
  }

  /* Brand name set as text */
  .brand {
    display: flex; align-items: center; gap: 10px;
    color: var(--green); font-weight: 600; font-size: 28px;
    letter-spacing: .5px; white-space: nowrap;
  }
  .brand-dot { width: 16px; height: 16px; border-radius: 50%; background: var(--green); flex: none; }

  /* Back: appointment card */
  .card-back { background: var(--card-light); color: var(--text-dark); }
  .card-back .brand { position: absolute; top: 58px; left: 50%; transform: translateX(-50%); }
  .appt-title { position: absolute; top: 140px; width: 100%; text-align: center; font-size: 26px; font-weight: 600; }
  .appt-row {
    position: absolute; top: 206px; left: 0; width: 100%;
    display: flex; justify-content: center; gap: 34px;
  }
  .appt-line { font-size: 19px; font-weight: 600; display: flex; align-items: flex-end; gap: 6px; white-space: nowrap; }
  .appt-line .dots { width: 140px; height: 18px; border-bottom: 2px dotted var(--text-dark); }
  .appt-notice { position: absolute; top: 290px; width: 100%; text-align: center; color: var(--green); font-weight: 700; font-size: 19px; }

  /* Front: dentist card */
  .card-front { background: var(--card-dark); color: var(--text-light); }
  .front-bands { position: absolute; inset: 0; }
  .dentist { position: absolute; top: 28px; left: 78px; }
  .dentist-name { color: var(--green); font-weight: 700; font-size: 22px; }
  .dentist-quals { font-size: 14px; margin-top: 2px; }
  .card-front .brand { position: absolute; top: 150px; right: 40px; }
  .contact { position: absolute; top: 130px; left: 34px; font-size: 14.5px; line-height: 22px; list-style: none; }
  .contact .address { margin-bottom: 6px; padding-left: 22px; display: block; }
  .contact li { display: flex; align-items: center; gap: 8px; }
  .contact svg { width: 14px; height: 14px; flex: none; fill: var(--green); }
</style>
</head>
<body>
<main class="stage">

  <section class="card card-back" aria-label="Appointment card">
    <div class="brand"><span class="brand-dot"></span>Maple Dental Centre</div>
    <h2 class="appt-title">Your Next Appointment on</h2>
    <div class="appt-row">
      <p class="appt-line">Date :<span class="dots"></span></p>
      <p class="appt-line">Time :<span class="dots"></span>AM / PM</p>
    </div>
    <p class="appt-notice">If unable to keep appointment, kindly give 24hrs notice.</p>
  </section>

  <section class="card card-front" aria-label="Dentist business card">
    <svg class="front-bands" viewBox="0 0 640 391" preserveAspectRatio="none" aria-hidden="true">
      <polygon points="30,28 56,28 44,56 30,56" fill="var(--green)"/>
      <polygon points="56,28 66,28 54,56 44,56" fill="var(--grey)"/>
      <polygon points="0,300 240,318 228,340 0,340" fill="var(--grey)"/>
      <polygon points="246,318 640,346 640,391 226,391 238,340" fill="var(--green)"/>
    </svg>
    <div class="dentist">
      <h1 class="dentist-name">Dr Priyanka R Valtenhoff</h1>
      <p class="dentist-quals">B.D.Sc., M.Sc (Kelv)</p>
    </div>
    <div class="brand"><span class="brand-dot"></span>Maple Dental Centre</div>
    <ul class="contact">
      <li class="address">117C, 48 Harlow Street,<br>Kelvona - 4821, Queensland</li>
      <li><svg viewBox="0 0 24 24"><path d="M6.6 10.8a15 15 0 0 0 6.6 6.6l2.2-2.2a1 1 0 0 1 1-.25 11 11 0 0 0 3.6.6 1 1 0 0 1 1 1V20a1 1 0 0 1-1 1A17 17 0 0 1 3 4a1 1 0 0 1 1-1h3.5a1 1 0 0 1 1 1 11 11 0 0 0 .6 3.6 1 1 0 0 1-.25 1z"/></svg>07- 5581 2943</li>
      <li><svg viewBox="0 0 24 24"><path d="M2 5h20v14H2z M2 5l10 8 10-8"/></svg>admin@mapledentalcentrekelvona.example.au</li>
      <li><svg viewBox="0 0 24 24"><circle cx="12" cy="12" r="10"/></svg>www.mapledentalcentre.example.au</li>
    </ul>
  </section>

</main>
</body>
</html>
```